Re-design Consulting Web Site (B2B Sales Consultancy for Early Stage SaaS/tech firms)

I have just built a web site in WordPress.

Here is the link:- https://tawny-walrus-518306.sitehaven.example/

(ALL PAGES AND SITE CONTENT IS FOUND ON THE LINK)

It's not a bad site. It's just a bit messy in terms of consistency and styling - font usage, spacing between sections etc. I want it to be slick, stylish and professional.

My audience is CEOs/Founders of B2B Tech / SaaS firms.

One of the issues is font choice and inconsistent font sizing maybe.

The site is currently in WordPress but I don't mind it being built outside of WordPress provided it will be easy to manage and update.

Some designs I kind of like (although do not just copy these - I want original designs).
https://layouts.brisklane.example/ko/office4/
https://fernpath.lumidock.example/ledger-advisory/

OTHER NOTES:

I don't to use too many photos on the new design. We can keep the photos where I am shown.

I would like to use more custom graphics and abstract graphics.

NOTE: One designer started a design in Figma but she had a family emergency and had to cancel the project. She what she did. It's ok - https://www.draftloom.example/design/q7Tzw2PLmkXvB4hNcYsAeG/Untitled?node-id=0-1

Target Market(s)

CEOs / Founders of B2B SaaS firms in the UK and US

Industry/Entity Type

SaaS, Tech, Consulting, Coaching, IT, Management Consulting.

Number of Pages Required

5+ page

Font styles to use
Serif
Sans Serif
Other font styles liked:
• Poppins or something similar/better.

Colors

Designer to choose colors to be used in the design.

Requirements
Must have
• Impactful headlines. Reorganise the information presented on my current side much better. Spacings and alignments must be spot on. Use Poppins as the font (or something similar). Abstract/custom graphics. A nice colour palette with 3-4 colors. the 'Engagement Plans' section on the homepage needs to be redesigned completely so the information is presented almost in accordian style or someting.
Nice to have
• Try graph paper style as the header background. See this Figma design one designer started - https://www.draftloom.example/design/q7Tzw2PLmkXvB4hNcYsAeG/Untitled?node-id=0-1
Should not have
• Do not use Merriweather, Roboto or Aria fonts. No not use red. Please do NOT simply present the existing UI, design and Information Architecture in the same or similar form as the current site. This defeats the purpose. I want to see NEW designs and a better way of organising and presenting the existing site content.

```html
<!DOCTYPE html>
<html lang="en">
<head>
<meta charset="utf-8">
<title>About – SaaS Sales Consultancy</title>
<link href="https://fonts.googleapis.com/css2?family=Poppins:wght@300;400;500;600;700&display=swap" rel="stylesheet">
<style>
:root{
  --navy:#0b1a6b;
  --navy-deep:#001a66;
  --ink:#111111;
  --grey-text:#7a7a7a;
  --mission-card:rgba(226,230,237,0.93);
  --rule:#bfc3cc;
  --white:#ffffff;
}
*{margin:0;padding:0;box-sizing:border-box}
html,body{width:1200px;height:3125px;overflow:hidden;background:var(--white)}
body{position:relative;font-family:'Poppins',sans-serif;color:var(--ink)}

.site-nav{position:absolute;top:0;left:0;width:1200px;height:58px;background:var(--white);border-bottom:1px solid #e6e6e6}
.social-links{position:absolute;left:155px;top:25px;display:flex;gap:6px}
.social-links span{width:8px;height:8px;background:var(--ink);display:block;border-radius:1px}
.nav-link{position:absolute;top:22px;font-size:11px;color:var(--ink);text-decoration:none}
.nav-link.active{top:0;height:58px;width:59px;background:#000;color:var(--white);display:flex;align-items:center;justify-content:center}
.nav-search{position:absolute;left:1031px;top:22px}

.hero-banner{position:absolute;top:58px;left:0;width:1200px;height:392px;
  background:radial-gradient(ellipse at 50% 45%,#1aa7d8 0%,#0b5fb3 38%,#072f7a 70%,#020a2a 100%)}

.highlight{position:absolute;top:490px;left:155px;width:888px;text-align:center}
.highlight h1{font-weight:300;font-size:51px;color:var(--navy);line-height:1.2;letter-spacing:0.5px}
.highlight p{margin-top:18px;font-weight:300;font-size:20.5px;line-height:27.5px;color:var(--grey-text)}

.mission-band{position:absolute;top:869px;left:0;width:1200px;height:805px;
  background:radial-gradient(ellipse at 30% 40%,#1b63b5 0%,#0b2f6e 45%,#05132f 100%)}
.mission-card{position:absolute;top:938px;left:155px;width:888px;height:667px;background:var(--mission-card);
  border-radius:55px 0 55px 0}
.mission-card h2{position:absolute;top:18px;left:0;width:100%;text-align:center;font-weight:300;font-size:53px;color:#000;line-height:1.2}
.mission-col{position:absolute;top:91px;width:380px;font-size:13.6px;font-weight:300;line-height:18.8px;color:#1a1a1a}
.mission-col p{margin-bottom:18.8px}
.mission-col strong{font-weight:600}
.col-left{left:48px}
.col-right{left:466px}

.contact-card{position:absolute;top:1780px;left:155px;width:420px;height:426px;background:var(--navy-deep);border-radius:42px}
.contact-eyebrow{position:absolute;left:39px;top:40px;font-size:10px;font-weight:600;letter-spacing:1.4px;color:var(--white)}
.contact-title{position:absolute;left:38px;top:58px;font-size:48px;font-weight:600;letter-spacing:-1.5px;color:var(--white);line-height:1.2}
.field{position:absolute;left:38px;width:346px;border:1px solid #c9cfe6;border-radius:3px;font-size:9.5px;color:#c9cfe6;padding:6px 10px}
.send-btn{position:absolute;left:38px;top:361px;width:51px;height:24px;background:var(--white);color:var(--navy-deep);font-size:8px;font-weight:600;display:flex;align-items:center;justify-content:center}

.team-photo{position:absolute;top:1780px;left:621px;width:422px;height:426px;border-radius:42px;
  background:linear-gradient(160deg,#d8d8d8 0%,#8e8e8e 50%,#3b3b3b 100%)}

.arr-signup{position:absolute;left:155px;top:2282px}
.arr-signup h2{font-weight:400;font-size:51px;line-height:57px;color:var(--navy)}
.arr-signup p{margin-top:4px;font-weight:300;font-size:20px;color:var(--grey-text)}
.email-row{position:absolute;left:154px;top:2491px;width:334px;height:29px}
.email-input{position:absolute;left:0;top:0;width:260px;height:29px;border:1px solid #9a9a9a;border-radius:15px 0 0 15px;font-size:13px;color:#444;padding:5px 13px}
.email-btn{position:absolute;left:248px;top:-2px;width:86px;height:33px;background:var(--navy-deep);border-radius:14px;color:var(--white);font-size:13px;font-weight:500;display:flex;align-items:center;justify-content:center}

.video-frame{position:absolute;top:2291px;left:621px;width:421px;height:236px;
  background:linear-gradient(90deg,#b9b2a6 0%,#d8d4cf 40%,#e8e6e3 65%,#8a6b4e 100%)}
.play-btn{position:absolute;left:186px;top:93px}

.site-footer{position:absolute;top:3066px;left:155px;width:888px;border-top:1px solid var(--rule)}
.footer-link{position:absolute;top:24px;font-size:10.5px;color:#555;text-decoration:none;white-space:nowrap}
</style>
</head>
<body>

<header class="site-nav">
  <div class="social-links" aria-label="Social links"><span></span><span></span><span></span><span></span></div>
  <a class="nav-link" style="left:246px" href="#">Main Home Page</a>
  <a class="nav-link" style="left:421px" href="#">Founders &amp; CEOs</a>
  <a class="nav-link" style="left:591px" href="#">Sales Acceleration</a>
  <a class="nav-link" style="left:774px" href="#">SaaS Sales Leaders</a>
  <a class="nav-link active" style="left:957px" href="#">About</a>
  <svg class="nav-search" width="12" height="12" viewBox="0 0 12 12" aria-label="Search"><circle cx="5" cy="5" r="3.8" fill="none" stroke="#111" stroke-width="1.5"/><line x1="7.8" y1="7.8" x2="11" y2="11" stroke="#111" stroke-width="1.6"/></svg>
</header>

<div class="hero-banner" role="img" aria-label="Abstract blue network graphic with the year 2023 in large glowing numerals"></div>

<section class="highlight">
  <h1>2023 HIGHLIGHT</h1>
  <p>The mission was to help a SaaS startup in the sustainability and construction space achieve the necessary sales metrics to secure an ambitious Series A funding round in one of the most challenging VC markets on record. Mission Accomplished - Kestrelbuild has just raised $9.1M in a Series A funding. Increased MRR from $27k to $103k in 7 months; developed a GTM strategy to instill investor confidence and secure the funding round; reduced the sales cycle from 6 months to 3 months; restructured the Sales team and Customer Success functions, personally closed a £1.2M Enterprise deal; embedded a new sales process and methodology; coached the existing sales team to exceed targets for 5 consecutive months and built a set of sales metrics and forecasts for sales management and Board reporting.</p>
</section>

<div class="mission-band" role="img" aria-label="Deep blue abstract globe with glowing network connections"></div>
<section class="mission-card">
  <h2>OUR MISSION</h2>
  <div class="mission-col col-left">
    <p><strong>Making it easy for SaaS / software firms to acquire new customers on scale – with predictable consis</strong></p>
    <p>There's nothing I like more than hearing than hearing the sales bell ring *DING DING*</p>
    <p>I was in awe of top performing sales reps for all the. That's what prompted to leave a top 5 consulting firm after graduating from Kingsbridge University College (KUC) and join a leading startup in the start of the dot.com era. Selling is the toughest gig ever! I realized that the best sales professionals weren't the ones who worked the hardest, nor were they just simply lucky. It became my obsession to crack the code and rise from the middle of the pack to being a top performer myself – consistently – and I did.</p>
    <p>Did you know that The Revenue Leaders Guild reports that <strong>sales coaching</strong> ranks as the #1 activity to impact sales effectiveness but only 15% of managers say they have the right amount of coaching at their organization. In fact, <strong>94% of sales reps who achieve exceptional coaching hit their quotas*</strong></p>
    <p>I was coached and mentored by the best complex, consultative software sellers in Corvane Software and Halden Electric and my career took off. Now, I want the same for the individual sales reps, sales leaders and founder/CEOs that I work with – I want you to be the catalyst for hypergrowth.</p>
  </div>
  <div class="mission-col col-right">
    <p>I have been a top individual contributor for 8 years - Closed over $22m in software and SaaS sales - Instrumental in helping 3 startups scale and achieve a premium exit. Fourframe was acquired by Vantage Site Software which was later acquired by the $3.6B giant, Tremont.</p>
    <p>Over the last 14 years, I have developed, coached and scaled SaaS and Enterprise Software sales teams across the UK, Europe, US and the Middle East. As a Global Revenue Leader I have built high-performance sales teams for tech startups and scales-ups in the Construction, PropTech, Enterprise Asset Management and Facilities Management sectors. One team that I coached and mentored during the second wave of the COVID pandemic is still closing over 300 deals per month!</p>
    <p>The solutions I have helped launch and scale include: Augmented Reality, CAFM, ERP, BIM, Collaboration, Document Management, Project Management to name but a few.</p>
  </div>
</section>

<section class="contact-card">
  <div class="contact-eyebrow">-&nbsp; READY TO START</div>
  <div class="contact-title">Let’s Talk</div>
  <div class="field" style="top:114px;height:28px">Name</div>
  <div class="field" style="top:150px;height:28px">Email</div>
  <div class="field" style="top:186px;height:28px">Phone</div>
  <div class="field" style="top:221px;height:63px">I'm interested in</div>
  <div class="field" style="top:291px;height:63px">Other Notes</div>
  <div class="send-btn">SEND</div>
</section>

<div class="team-photo" role="img" aria-label="Black and white photo of two colleagues working at laptops around a table"></div>

<section class="arr-signup">
  <h2>Unlock 4<br>Strategies<br>to Boost ARR</h2>
  <p>Sign up to hear from us.</p>
</section>
<div class="email-row">
  <div class="email-input">Enter your e-mail</div>
  <div class="email-btn">SEE VIDEO</div>
</div>

<div class="video-frame" role="img" aria-label="Video still of the consultant presenting beside a flip chart">
  <svg class="play-btn" width="50" height="50" viewBox="0 0 50 50" aria-label="Play video"><circle cx="25" cy="25" r="22.5" fill="none" stroke="#111" stroke-width="3.5"/><polygon points="19,15 35,25 19,35" fill="#111"/></svg>
</div>

<footer class="site-footer">
  <a class="footer-link" style="left:67px" href="#">Main Home Page</a>
  <a class="footer-link" style="left:242px" href="#">Founders &amp; CEOs</a>
  <a class="footer-link" style="left:410px" href="#">Sales Acceleration</a>
  <a class="footer-link" style="left:595px" href="#">SaaS Sales Leaders</a>
  <a class="footer-link" style="left:790px" href="#">About</a>
</footer>

</body>
</html>
```